Plumbing Service Flyer Needed For Swapboard

Plumbing ad needs to be effective (600 by 450 pixels)
Ad must include company name Plumbing Aces and phone number 202-555-0187
No URLs, links, or web addresses in your text or image please.

(about us we offer a wide range of plumbing services from emergency plumbing to commercial plumbing services, our master plumbers are ready to handle all jobs, large or small, at anytime during the day or night. Pickup the phone and call us today).

Target Market(s)

DC Metro Area

Industry/Entity Type

Plumbing

Font styles to use
Other font styles liked:
• No preference. Let the designer choose

Colors

Designer to choose colors to be used in the design.

Requirements
Must have
• 1. A bold headline: headline should communicate what my business is all about.
• 2. Great photography
• 3. Discounts or specials
• 4. Call to action
• 5. Key facts: Let consumers know about the product or service (see attached ad)
• 6. Good graphics
Should not have
• No URLs, links, or web addresses in your text or image please.

```html
<!DOCTYPE html>
<html lang="en">
<head>
<meta charset="utf-8">
<title>Plumbing Aces – Flyer Concepts</title>
<link href="https://fonts.googleapis.com/css2?family=Bebas+Neue&family=Oswald:wght@500;600&family=Lato:ital,wght@0,400;0,700;0,900;1,400;1,700&display=swap" rel="stylesheet">
<style>
:root{
  --bg:#2b2b2b;
  --navy:#1d2a5c;
  --royal:#1f5fb0;
  --yellow:#fcd116;
  --ink:#1a1a1a;
  --white:#ffffff;
  --teal:#0e5a78;
  --orange:#f05a28;
  --red:#e2202b;
  --grey:#d2d2d2;
  --photo-a:#4a5d8f;
  --photo-b:#c9a66b;
}
*{margin:0;padding:0;box-sizing:border-box}
html,body{width:775px;height:1200px;overflow:hidden;background:var(--bg)}
body{position:relative;font-family:'Lato',sans-serif}
.cond{font-family:'Bebas Neue','Oswald',sans-serif;text-transform:uppercase;line-height:1;white-space:nowrap;font-weight:400}
.concept-no{position:absolute;font-family:'Oswald',sans-serif;font-weight:600;font-size:100px;color:var(--white);line-height:1}
.flyer{position:absolute;overflow:hidden}
.decor{position:absolute;left:0;top:0;z-index:0}
.abs{position:absolute;z-index:2}
.photo{position:absolute;z-index:1;background:linear-gradient(180deg,var(--photo-b) 0%,var(--photo-a) 40%,#2c3a66 100%);border-radius:40% 40% 8px 8px/30% 30% 8px 8px}
.phone-icon{width:30px;height:30px;flex:none}
.fine{font-family:'Lato',sans-serif;font-style:italic;font-size:7px;text-transform:none;color:var(--ink);text-align:center;line-height:1.2}
.nowrap{white-space:nowrap}

/* Concept 1 */
.f1{left:21px;top:27px;width:490px;height:367px;background:var(--navy)}
.f1 .header{left:0;top:0;width:490px;height:56px;background:var(--yellow);display:flex;align-items:center;padding-left:22px;font-size:44px;gap:14px}
.f1 .header .dark{color:var(--ink)}
.f1 .header .light{color:var(--white)}
.f1 .about{left:188px;top:66px;width:290px;color:var(--white);font-size:7.6px;line-height:1.35}
.f1 .label{font-family:'Bebas Neue',sans-serif;color:var(--yellow);font-size:11px;text-transform:uppercase;margin-bottom:2px}
.f1 .services{left:235px;top:116px;width:250px}
.f1 .svc-cols{display:flex;gap:12px;margin-top:3px}
.f1 ul{list-style:none;color:var(--white);font-style:italic;font-size:7.2px;line-height:1.55;width:112px}
.f1 li{position:relative;padding-left:11px}
.f1 li::before{content:"";position:absolute;left:0;top:3px;width:6px;height:6px;border-radius:50%;background:var(--yellow)}
.f1 li.more{color:var(--yellow)}
.f1 li.more::before{display:none}
.f1 .brand{left:17px;top:235px;color:var(--ink)}
.f1 .brand .name{font-size:30px}
.f1 .brand .tag{font-family:'Lato',sans-serif;font-size:8px;color:var(--white);margin-top:1px}
.f1 .brand .cta{font-size:18px;margin-top:8px}
.f1 .phone{left:17px;top:297px;display:flex;align-items:center;gap:8px;font-family:'Bebas Neue',sans-serif;font-size:46px;line-height:1;color:var(--ink);white-space:nowrap}
.f1 .badge{left:267px;top:206px;width:158px;height:140px}
.f1 .badge-text{left:267px;top:220px;width:158px;text-align:center;color:var(--red)}
.f1 .foot{left:0;top:345px;width:490px;height:22px;background:var(--royal)}

/* shared offer lockup */
.offer{display:flex;align-items:center;justify-content:center;font-family:'Bebas Neue',sans-serif;color:var(--ink);line-height:.9;white-space:nowrap}
.offer .off{writing-mode:vertical-rl;transform:rotate(180deg)}

/* Concept 2 */
.f2{left:198px;top:410px;width:509px;height:380px;background:var(--teal)}
.f2 .h1{left:23px;top:20px;font-size:60px;color:var(--white)}
.f2 .h2{left:22px;top:76px;font-family:'Lato',sans-serif;font-weight:900;font-size:31px;color:var(--orange);text-transform:uppercase;white-space:nowrap}
.f2 .band{left:0;top:129px;width:305px;height:47px;background:var(--grey);padding:5px 0 0 23px}
.f2 .band .s{font-size:15px;color:var(--ink)}
.f2 .band .b{font-family:'Lato',sans-serif;font-weight:900;font-size:24px;color:var(--orange);text-transform:uppercase;line-height:1.05;white-space:nowrap}
.f2 .body{left:25px;top:186px;width:278px;color:var(--white);font-size:10px;line-height:1.27;text-align:justify}
.f2 .ctabar{left:0;top:313px;width:509px;height:48px;display:flex}
.f2 .ctabar .l{width:250px;background:var(--white);display:flex;align-items:center;padding-left:18px;font-size:19px;color:var(--ink)}
.f2 .ctabar .r{flex:1;background:#2a2a2a;display:flex;align-items:center;gap:8px;padding-left:12px;font-family:'Bebas Neue',sans-serif;font-size:38px;line-height:1;color:var(--white);white-space:nowrap}
.f2 .foot{left:0;top:361px;width:509px;height:19px;background:linear-gradient(90deg,var(--red),var(--orange) 60%,#e54a26)}

/* Concept 3 */
.f3{left:21px;top:804px;width:510px;height:381px;background:linear-gradient(160deg,#1b64b8,#103f86 70%)}
.f3 .copy{right:18px;top:32px;text-align:right;color:var(--white)}
.f3 .copy .k{font-size:20px}
.f3 .copy .big{font-size:40px;color:var(--red);margin-top:4px}
.f3 .copy .sub{font-family:'Lato',sans-serif;font-weight:700;font-size:20px;text-transform:uppercase;margin-top:2px;white-space:nowrap}
.f3 .copy p{font-style:italic;font-size:14px;line-height:1.3;margin-top:12px}
.f3 .badge{left:42px;top:256px;width:114px;height:114px;border-radius:50%;background:var(--yellow);border:4px solid var(--white);box-shadow:0 0 0 2px #555;display:flex;flex-direction:column;align-items:center;justify-content:center;color:var(--red)}
.f3 .cta{right:24px;top:268px;text-align:right;color:var(--white)}
.f3 .cta .a{font-size:18px}
.f3 .cta .b{font-size:29px}
.f3 .cta .phone{display:flex;align-items:center;justify-content:flex-end;gap:8px;font-family:'Bebas Neue',sans-serif;font-size:46px;line-height:1;margin-top:4px;white-space:nowrap}
</style>
</head>
<body>

<div class="concept-no" style="left:529px;top:40px">1</div>
<div class="concept-no" style="left:131px;top:448px">2</div>
<div class="concept-no" style="left:552px;top:823px">3</div>

<!-- Concept 1 -->
<section class="flyer f1">
  <svg class="decor" width="490" height="367" viewBox="0 0 490 367">
    <path d="M0 225 C90 195 190 200 260 250 C320 290 390 310 490 300 L490 367 L0 367 Z" fill="#fcd116"/>
    <path d="M40 212 C130 185 220 200 290 255 C330 290 380 305 490 305 L490 315 C380 316 320 300 280 268 C210 215 130 195 40 222 Z" fill="#111"/>
    <path d="M90 200 C170 180 250 195 320 245 C360 272 410 288 490 286 L490 298 C400 300 350 284 310 256 C240 208 170 190 90 208 Z" fill="#1f5fb0"/>
    <path d="M150 196 C220 186 280 200 340 235 C380 258 420 270 490 270 L490 280 C420 282 370 268 330 244 C270 208 220 196 150 202 Z" fill="#fff"/>
  </svg>
  <div class="photo" role="img" aria-label="Photo of a smiling plumber in hard hat and overalls holding a pipe wrench" style="left:45px;top:62px;width:170px;height:150px"></div>
  <div class="abs header cond"><span class="dark">24/7 Plumber</span><span class="light">At Your Service!</span></div>
  <div class="abs about">
    <div class="label">About Us</div>
    we offer a wide range of plumbing services from emergency plumbing to commercial plumbing services, our master plumbers are ready to handle all jobs, large or small, at anytime during the day or night.
  </div>
  <div class="abs services">
    <div class="label">Here are a few of my plumbing services:</div>
    <div class="svc-cols">
      <ul><li>Plumbing clogs</li><li>Water heater replacement</li><li>Repair and install gas lines</li><li>Remodel your plumbing</li><li>Flood repair</li></ul>
      <ul><li>Disposals repair and install</li><li>Toilets install or replace</li><li>New piping and repairs</li><li>New homes, old homes, commercial plumbing</li><li class="more">and a ton more</li></ul>
    </div>
  </div>
  <div class="abs brand cond">
    <div class="name">Plumbing Aces</div>
    <div class="tag">BONDED, LICENSED AND INSURED</div>
    <div class="cta">Pickup the phone and call us today</div>
  </div>
  <div class="abs phone">
    <svg class="phone-icon" viewBox="0 0 30 30"><circle cx="15" cy="15" r="13" fill="#fff"/><path d="M9 8c2-2 4 2 4 3s-2 2-1 4 3 4 4 4 2-2 3-1 3 3 1 4c-6 3-14-8-11-14z" fill="#fcd116"/></svg>
    202-555-0187
  </div>
  <svg class="abs badge" viewBox="0 0 158 140"><path d="M4 14 L79 2 L154 14 L150 90 C140 115 100 130 79 138 C58 130 18 115 8 90 Z" fill="#1f5fb0"/><path d="M12 19 L79 9 L146 19 L142 88 C133 110 98 123 79 130 C60 123 25 110 16 88 Z" fill="#e8e8ea"/></svg>
  <div class="abs badge-text">
    <div class="cond" style="font-size:26px">Special Offer</div>
    <div class="offer"><span style="font-size:50px">$25</span><span class="off" style="font-size:16px">OFF</span></div>
    <div class="cond" style="font-size:15px;margin-top:2px">Any Plumbing Service</div>
    <div class="fine" style="margin-top:3px">*Offer Applies to projects<br>$250 or more</div>
  </div>
  <div class="abs foot"></div>
</section>

<!-- Concept 2 -->
<section class="flyer f2">
  <svg class="decor" width="509" height="380" viewBox="0 0 509 380">
    <path d="M0 245 C120 290 300 300 509 255 L509 313 L0 313 Z" fill="#e2202b"/>
    <path d="M0 258 C130 300 300 306 509 262 L509 313 L0 313 Z" fill="#f05a28"/>
    <path d="M0 240 C120 282 300 292 509 248 L509 254 C300 298 120 290 0 248 Z" fill="#fff"/>
    <ellipse cx="259" cy="285" rx="110" ry="30" fill="#fcd116"/>
  </svg>
  <div class="photo" role="img" aria-label="Photo of a smiling plumber in hard hat and overalls holding a pipe wrench" style="left:330px;top:18px;width:165px;height:255px"></div>
  <div class="abs h1 cond">24/7 Plumber</div>
  <div class="abs h2">At Your Service!</div>
  <div class="abs band"><div class="s cond">Whatever the size of your plumbing problem,</div><div class="b">We can handle it!</div></div>
  <div class="abs body">Our experienced, professional plumbers will come out to your home or business and deliver quality service. We service the entire metropolitan area. We are available 24/7 and your satisfaction is our highest priority.</div>
  <div class="abs" style="left:185px;top:262px;width:160px">
    <div class="offer" style="justify-content:flex-start"><span style="font-size:34px;color:var(--red)">$25</span><span class="off" style="font-size:11px">OFF</span><span class="cond" style="font-size:13px;margin-left:4px;line-height:.95">Any Plumbing<br><span style="font-size:17px">Service</span></span></div>
  </div>
  <div class="abs fine" style="left:150px;top:296px;width:218px">*Offer Applies to projects $250 or more</div>
  <div class="abs ctabar">
    <div class="l cond">Pickup the phone and call us today</div>
    <div class="r">
      <svg class="phone-icon" viewBox="0 0 30 30"><circle cx="15" cy="15" r="13" fill="none" stroke="#fff" stroke-width="2"/><path d="M9 8c2-2 4 2 4 3s-2 2-1 4 3 4 4 4 2-2 3-1 3 3 1 4c-6 3-14-8-11-14z" fill="#fff"/></svg>
      (571) 555-0142
    </div>
  </div>
  <div class="abs foot"></div>
</section>

<!-- Concept 3 -->
<section class="flyer f3">
  <svg class="decor" width="510" height="381" viewBox="0 0 510 381">
    <path d="M0 300 C150 250 330 250 510 262 L510 381 L0 381 Z" fill="#d71f2a"/>
    <path d="M0 285 C150 240 330 240 510 250 L510 260 C330 250 150 252 0 300 Z" fill="#fff"/>
    <path d="M0 278 C150 232 330 232 510 242 L510 250 C330 240 150 240 0 285 Z" fill="#1f5fb0"/>
  </svg>
  <div class="photo" role="img" aria-label="Photo of a smiling plumber in hard hat and overalls holding a pipe wrench" style="left:22px;top:10px;width:180px;height:255px"></div>
  <div class="abs copy">
    <div class="cond k">Our dedicated, experienced plumbers offer</div>
    <div class="cond big">Fast, Friendly Service</div>
    <div class="sub">To your home or business.</div>
    <p>No matter what the plumbing problem,<br>we can fix it for you!</p>
    <p>We are available day or night and<br>we offer immediate, same-day service.</p>
  </div>
  <div class="abs badge">
    <div class="cond" style="font-size:17px">Special Offer</div>
    <div class="offer"><span style="font-size:34px">$25</span><span class="off" style="font-size:11px">OFF</span></div>
    <div class="cond" style="font-size:10px">Any Plumbing Service</div>
    <div class="fine" style="font-size:6.5px;margin-top:2px">*Offer Applies to projects<br>$250 or more</div>
  </div>
  <div class="abs cta">
    <div class="cond a">Pickup the phone and</div>
    <div class="cond b">Call us today</div>
    <div class="phone">
      <svg class="phone-icon" viewBox="0 0 30 30"><circle cx="15" cy="15" r="13" fill="#fff"/><path d="M9 8c2-2 4 2 4 3s-2 2-1 4 3 4 4 4 2-2 3-1 3 3 1 4c-6 3-14-8-11-14z" fill="#d71f2a"/></svg>
      (202) 555-0163
    </div>
  </div>
</section>

</body>
</html>
```